Sign Advertisment for Condominium Development

I need a sign created that will be placed in front of a building that is being converted into a luxury condominium development.

The sign needs to say:

Two, Boutique Luxury Condominiums Delivering late 2015.

Luxury Finishes // Designer Kitchens and Bath // Each Unit over 2,000 Square Feet

Deeded Parking Included with Each Unit

To Learn More, Contact:

Marissa Talbot or Vernon Pike
(202) 555-0147
Marissa.Talbot@example-realty.com

I need a small disclaimer at the bottom stating:

These Condominium(s) have not been registered by the Office of Residential Standards and Property Oversight Bureau Tenancy Transition and Transfer Section. A Condominium Unit may be reserved on a non-binding reservation agreement, but no contract of sale or lease that is binding on the purchaser may be entered into prior to registration.

Target Market(s)

Young professionals seeking luxury condominium

Industry/Entity Type

Building

Font styles to use
Serif

Colors
00a88f
ffffff

```html
<!DOCTYPE html>
<html lang="en">
<head>
<meta charset="utf-8">
<title>Harborline Fine Properties – Boutique Luxury Condominiums</title>
<link href="https://fonts.googleapis.com/css2?family=Open+Sans:ital,wght@0,400;0,600;1,300&display=swap" rel="stylesheet">
<style>
  :root {
    --navy: #25243b;
    --paper: #ffffff;
    --ink: #2a2a35;
    --ink-soft: #3a3a48;
    --photo-top: #a7c4e2;
    --photo-mid: #9fb7cc;
    --photo-low: #b9b29a;
  }
  * { margin: 0; padding: 0; box-sizing: border-box; }
  html, body { width: 1200px; height: 800px; overflow: hidden; background: var(--paper); }
  body { font-family: "Open Sans", Arial, sans-serif; color: var(--ink); }

  .sign { position: relative; width: 1200px; height: 800px; }

  .info-column { position: absolute; left: 0; top: 0; width: 450px; height: 800px; background: var(--paper); }

  .brand-band {
    height: 175px; background: var(--navy);
    display: flex; flex-direction: column; align-items: center; justify-content: center;
    padding-right: 30px; padding-top: 42px;
  }
  .brand-name {
    color: var(--paper); font-weight: 600; font-size: 28px; letter-spacing: 0.5px; line-height: 1;
  }
  .brand-sub {
    color: var(--paper); font-weight: 600; font-size: 13px; letter-spacing: 0.6px; margin-top: 4px;
  }

  .headline {
    position: absolute; left: 48px; top: 207px;
    font-weight: 300; font-style: italic; font-size: 34px; line-height: 44px; color: var(--ink);
  }

  .features {
    position: absolute; left: 30px; top: 379px; list-style: none;
    font-size: 18px; line-height: 25px; color: var(--ink-soft);
  }
  .features li { position: relative; padding-left: 18px; }
  .features li::before {
    content: ""; position: absolute; left: 0; top: 9px;
    width: 8px; height: 8px; border-radius: 50%; background: var(--navy);
  }

  .contact { position: absolute; left: 48px; top: 566px; font-size: 14px; line-height: 20px; color: var(--ink); }

  .disclaimer-band {
    position: absolute; left: 0; top: 632px; width: 450px; height: 168px;
    background: var(--navy); padding: 20px 23px 0 28px;
  }
  .disclaimer {
    color: var(--paper); font-size: 13.6px; line-height: 20px; text-align: justify;
  }

  .lifestyle-photo {
    position: absolute; left: 450px; top: 0; width: 750px; height: 800px;
    background: linear-gradient(180deg, var(--photo-top) 0%, var(--photo-mid) 50%, var(--photo-low) 100%);
  }
</style>
</head>
<body>
  <main class="sign">
    <section class="info-column">
      <header class="brand-band">
        <div class="brand-name">HARBORLINE</div>
        <div class="brand-sub">FINE PROPERTIES, LLC</div>
      </header>

      <h1 class="headline">Two, Boutique Luxury<br>Condominiums<br>Delivering late 2015.</h1>

      <ul class="features">
        <li>Luxury Finishes</li>
        <li>Designer Kitchens and Bath</li>
        <li>Each Unit over 2,000 Square Feet</li>
        <li>Deeded Parking Included with Each Unit</li>
      </ul>

      <div class="contact">
        <p>To Learn More, Contact:</p>
        <p>Marissa Talbot or Vernon Pike</p>
        <p>(202) 555-0147 Marissa.Talbot@example-realty.com</p>
      </div>

      <footer class="disclaimer-band">
        <p class="disclaimer">These Condominium(s) have not been registered by the Office of Residential Standards and Property Oversight Bureau Tenancy Transition and Transfer Section. A Condominium Unit may be reserved on a non-binding reservation agreement, but no contract of sale or lease that is binding on the purchaser may be entered into prior to registration.</p>
      </footer>
    </section>

    <div class="lifestyle-photo" role="img" aria-label="Photo of a woman in swimwear holding a wrap beside a plunge pool on a covered wooden terrace with cushioned seating, overlooking the open ocean under a blue sky"></div>
  </main>
</body>
</html>
```